Business card and stationary design for construction company
RT Garland Construction
Business card and stationary design for construction company - Construction
Creative Brief
Professional
Marcus Garland
President
781 Willow Bend Dr Santa Rosa Beach, FL 32617
marcus@rt-garland.example
rt-garland.example

```html
<!DOCTYPE html>
<html lang="en">
<head>
<meta charset="utf-8">
<title>RT Garland Construction — Business Card</title>
<link rel="stylesheet" href="https://fonts.googleapis.com/css2?family=Open+Sans:wght@300;400;600;700&display=swap">
<style>
  :root {
    --page: #e4e5e6;
    --card-white: #ffffff;
    --brand-blue: #2a7fae;
    --brand-navy: #1f5fa3;
    --brand-ink: #1b4f86;
    --text-white: #ffffff;
    --text-soft: #d6e8f3;
  }
  * { box-sizing: border-box; margin: 0; padding: 0; }
  html, body {
    width: 1200px; height: 842px; overflow: hidden;
    background: var(--page);
    font-family: "Open Sans", Arial, sans-serif;
  }
  .sheet {
    position: relative; width: 1200px; height: 842px;
    display: flex; align-items: center; justify-content: center; gap: 40px;
  }
  .card {
    position: relative; width: 540px; height: 309px; overflow: hidden;
    box-shadow: 0 2px 8px rgba(0,0,0,0.12);
  }

  /* Front */
  .card-front { background: var(--card-white); }
  .brand-lockup {
    position: absolute; top: 34px; left: 0; width: 100%;
    display: flex; align-items: center; justify-content: center; gap: 8px;
  }
  .brand-square { width: 22px; height: 22px; background: var(--brand-ink); }
  .brand-name {
    font-weight: 700; font-size: 19px; color: var(--brand-ink);
    letter-spacing: 0.5px; text-transform: uppercase;
  }
  .name-band {
    position: absolute; left: 0; top: 116px; width: 232px; height: 42px;
    background: var(--brand-navy); color: var(--text-white);
    padding: 5px 0 0 62px;
  }
  .person-name { font-weight: 700; font-size: 13px; line-height: 1.25; }
  .person-title { font-weight: 400; font-size: 11px; line-height: 1.3; }
  .address-panel {
    position: absolute; left: 0; top: 158px; width: 254px; height: 151px;
    background: var(--brand-blue); color: var(--text-white);
    padding: 18px 0 0 62px; font-size: 11px; line-height: 1.5;
  }
  .contact-panel {
    position: absolute; left: 282px; top: 194px; width: 258px; height: 115px;
    background: var(--brand-blue); color: var(--text-white);
    padding: 16px 0 0 20px; font-size: 11px;
  }
  .contact-row { display: flex; align-items: center; gap: 8px; height: 19px; }
  .contact-icon { width: 12px; height: 12px; flex: none; }

  /* Back */
  .card-back { background: var(--brand-blue); color: var(--text-white); }
  .services {
    position: absolute; top: 28px; left: 74px;
    font-weight: 300; font-size: 15px; line-height: 1.35;
  }
  .back-web {
    position: absolute; top: 118px; left: 74px;
    font-weight: 300; font-size: 10px; letter-spacing: 2px; color: var(--text-soft);
  }
  .back-brand {
    position: absolute; right: 22px; bottom: 22px;
    font-weight: 700; font-size: 22px; color: var(--text-soft);
    text-transform: uppercase; letter-spacing: 1px;
  }
</style>
</head>
<body>
<main class="sheet">
  <section class="card card-front" aria-label="Business card front">
    <div class="brand-lockup">
      <span class="brand-square"></span>
      <span class="brand-name">RT Garland Construction</span>
    </div>
    <div class="name-band">
      <p class="person-name">Marcus Garland</p>
      <p class="person-title">President</p>
    </div>
    <div class="address-panel">
      <p>781 Willow Bend Dr</p>
      <p>Cedar Hollow, GA 31587</p>
    </div>
    <div class="contact-panel">
      <p class="contact-row">
        <svg class="contact-icon" viewBox="0 0 12 12"><circle cx="6" cy="6" r="6" fill="#fff"/><path d="M4 3.2l1.2 1.3-.6.9c.4.8 1 1.4 1.8 1.8l.9-.6 1.3 1.2-.6.9c-2.1-.3-4-2.2-4.3-4.3z" fill="#2a7fae"/></svg>
        <span>555-210-0142</span>
      </p>
      <p class="contact-row">
        <svg class="contact-icon" viewBox="0 0 12 12"><circle cx="6" cy="6" r="6" fill="#fff"/><rect x="3" y="4" width="6" height="4.2" fill="none" stroke="#2a7fae" stroke-width="0.9"/><path d="M3 4l3 2.3L9 4" fill="none" stroke="#2a7fae" stroke-width="0.9"/></svg>
        <span>marcus@rt-garland.example</span>
      </p>
      <p class="contact-row">
        <svg class="contact-icon" viewBox="0 0 12 12"><circle cx="6" cy="6" r="6" fill="#fff"/><circle cx="6" cy="6" r="3.2" fill="none" stroke="#2a7fae" stroke-width="0.8"/><path d="M2.8 6h6.4M6 2.8c-1.4 1.8-1.4 4.6 0 6.4M6 2.8c1.4 1.8 1.4 4.6 0 6.4" fill="none" stroke="#2a7fae" stroke-width="0.7"/></svg>
        <span>www.rt-garland.example</span>
      </p>
    </div>
  </section>

  <section class="card card-back" aria-label="Business card back">
    <div class="services">
      <p>Commercial</p>
      <p>Industrial</p>
      <p>Residential</p>
    </div>
    <p class="back-web">www.rt-garland.example</p>
    <p class="back-brand">RT Garland</p>
  </section>
</main>
</body>
</html>
```